Business card design needed for Renewable utilities company based in New Zealand.

We supply and install solar panels and all components along with it for a fully customisable PV system that helps customer save money on their energy bills right away and also save the planet!

I have attached logo & website design files to give you a better insight.

Business

```html
<!DOCTYPE html>
<html lang="en">
<head>
<meta charset="utf-8">
<title>Sunward Grid – Business Card</title>
<link href="https://fonts.googleapis.com/css2?family=Questrial&family=Cinzel:wght@500&display=swap" rel="stylesheet">
<style>
  :root {
    --backdrop: #d9dcdf;
    --navy-deep: #0d2c5c;
    --navy: #173f7a;
    --blue: #1f5bb0;
    --blue-bright: #2a73cf;
    --ink: #2b2f36;
    --white: #ffffff;
    --map-tone: rgba(140, 170, 215, 0.18);
  }
  * { margin: 0; padding: 0; box-sizing: border-box; }
  html, body {
    width: 1200px;
    height: 871px;
    overflow: hidden;
    background: var(--backdrop);
  }
  .canvas {
    width: 1200px;
    height: 871px;
    display: flex;
    flex-direction: column;
    align-items: center;
    justify-content: center;
    gap: 44px;
  }
  .card {
    position: relative;
    width: 640px;
    height: 366px;
    overflow: hidden;
    box-shadow: 0 10px 28px rgba(0, 0, 0, 0.22);
  }

  /* Front */
  .card-front {
    background: linear-gradient(135deg, var(--navy) 0%, var(--navy-deep) 70%, #0a2249 100%);
  }
  .world-map-area {
    position: absolute;
    left: 40px;
    top: 60px;
    width: 560px;
    height: 250px;
    border-radius: 40px;
    background: radial-gradient(ellipse at center, var(--map-tone) 0%, rgba(140,170,215,0.06) 60%, transparent 80%);
  }
  .front-brand {
    position: absolute;
    left: 0;
    right: 0;
    top: 92px;
    display: flex;
    flex-direction: column;
    align-items: center;
    gap: 22px;
  }
  .brand-dot-light {
    width: 86px;
    height: 86px;
    border-radius: 50%;
    background: var(--white);
  }
  .brand-name-light {
    font-family: "Questrial", sans-serif;
    font-size: 44px;
    color: var(--white);
    letter-spacing: 0.5px;
  }

  /* Back */
  .card-back { background: var(--white); }
  .back-band {
    position: absolute;
    inset: 0;
  }
  .contact {
    position: absolute;
    left: 44px;
    top: 34px;
    color: var(--ink);
    font-family: "Questrial", sans-serif;
  }
  .contact-name {
    font-family: "Cinzel", serif;
    font-weight: 500;
    font-size: 17px;
    letter-spacing: 0.6px;
    color: var(--ink);
  }
  .contact-role {
    font-family: "Cinzel", serif;
    font-size: 12px;
    letter-spacing: 0.5px;
    color: var(--blue);
    margin-top: 1px;
  }
  .contact-address {
    font-size: 13px;
    line-height: 1.35;
    margin-top: 20px;
  }
  .contact-lines {
    list-style: none;
    margin-top: 16px;
    font-size: 13px;
    line-height: 1.55;
  }
  .contact-lines li {
    display: flex;
    align-items: center;
    gap: 10px;
  }
  .contact-icon { width: 12px; height: 12px; flex: none; }
  .back-brand {
    position: absolute;
    left: 380px;
    top: 78px;
    width: 230px;
    display: flex;
    flex-direction: column;
    align-items: center;
    gap: 14px;
  }
  .brand-dot-blue {
    width: 64px;
    height: 64px;
    border-radius: 50%;
    background: var(--blue);
  }
  .brand-name-blue {
    font-family: "Questrial", sans-serif;
    font-size: 30px;
    color: var(--blue);
  }
  .web-address {
    position: absolute;
    right: 36px;
    bottom: 26px;
    font-family: "Questrial", sans-serif;
    font-size: 15px;
    color: var(--white);
    letter-spacing: 0.4px;
  }
</style>
</head>
<body>
<main class="canvas">

  <section class="card card-front" aria-label="Business card front">
    <div class="world-map-area" role="img" aria-label="Faint dotted world map in the background"></div>
    <div class="front-brand">
      <span class="brand-dot-light"></span>
      <span class="brand-name-light">Sunward Grid</span>
    </div>
  </section>

  <section class="card card-back" aria-label="Business card back">
    <svg class="back-band" viewBox="0 0 640 366" preserveAspectRatio="none" aria-hidden="true">
      <defs>
        <linearGradient id="bandFill" x1="0" y1="0" x2="1" y2="1">
          <stop offset="0" stop-color="#2a73cf"/>
          <stop offset="1" stop-color="#143d7c"/>
        </linearGradient>
      </defs>
      <path d="M0,296 C190,338 450,330 640,170 L640,366 L0,366 Z" fill="url(#bandFill)"/>
      <path d="M0,286 C190,328 450,320 640,160" fill="none" stroke="#2a73cf" stroke-opacity="0.35" stroke-width="4"/>
    </svg>

    <div class="contact">
      <h1 class="contact-name">Daniel R. Hughes</h1>
      <p class="contact-role">Installer</p>
      <p class="contact-address">14 Kauri St. Unit 3<br>Auckland 1010, NZ</p>
      <ul class="contact-lines">
        <li>
          <svg class="contact-icon" viewBox="0 0 12 12" aria-hidden="true"><path d="M2,1 L4.5,1 L5.5,3.5 L4,4.5 Q5,7 7.5,8 L8.5,6.5 L11,7.5 L11,10 Q6,11 2.5,7 Q0.5,4 2,1 Z" fill="#1f5bb0"/></svg>
          09 555 0142
        </li>
        <li>
          <svg class="contact-icon" viewBox="0 0 12 12" aria-hidden="true"><rect x="3" y="0.5" width="6" height="11" rx="1.2" fill="#1f5bb0"/><rect x="4" y="2" width="4" height="6" fill="#fff"/></svg>
          021 555 0147
        </li>
        <li>
          <svg class="contact-icon" viewBox="0 0 12 12" aria-hidden="true"><rect x="0.5" y="2" width="11" height="8" rx="1" fill="#1f5bb0"/><path d="M1,2.5 L6,6.5 L11,2.5" fill="none" stroke="#fff" stroke-width="1"/></svg>
          daniel@sunwardgrid.co.nz
        </li>
      </ul>
    </div>

    <div class="back-brand">
      <span class="brand-dot-blue"></span>
      <span class="brand-name-blue">Sunward Grid</span>
    </div>

    <p class="web-address">www.sunwardgrid.co.nz</p>
  </section>

</main>
</body>
</html>
```